Torquel Australia Pty Ltd

I require professional business cards with our company logo. We would like something that looks sharp and unique. I have attached the logo for our business, which is an industrial electrical contracting company. But this does not need to be shown on the cards.

Industry/Entity Type

Industrial

Requirements
Must have
• The design must be double sided and needs to have one side with our logo only and the other side with our details.
Should not have
• We do not want any lightening bolts on the designs as this is very common.

```html
<!DOCTYPE html>
<html lang="en">
<head>
<meta charset="utf-8">
<title>Torquel Australia Pty Ltd – Business Cards</title>
<link rel="stylesheet" href="https://fonts.googleapis.com/css2?family=Archivo:wght@400;600;700&display=swap">
<style>
  :root {
    --bg: #e9e7e3;
    --card-dark: #0d0d0d;
    --card-light: #f1f1ef;
    --gold: #c49a3c;
    --ink: #1f1f1f;
    --ink-soft: #3a3a3a;
    --icon-fg: #ffffff;
  }
  * { margin: 0; padding: 0; box-sizing: border-box; }
  html, body {
    width: 1200px; height: 900px; overflow: hidden;
    background: var(--bg);
    font-family: "Archivo", Arial, sans-serif;
  }
  .canvas {
    position: relative; width: 1200px; height: 900px;
    display: flex; flex-direction: column; align-items: center; justify-content: center; gap: 60px;
  }
  .card {
    position: relative; width: 560px; height: 320px;
    box-shadow: 0 10px 30px rgba(0,0,0,0.18);
    overflow: hidden;
  }
  .card--front { background: var(--card-dark); }
  .card--back { background: var(--card-light); }

  .brand { position: absolute; display: flex; align-items: center; gap: 16px; }
  .brand__mark {
    width: 64px; height: 64px; border-radius: 50%;
    border: 5px solid var(--gold); flex: none;
  }
  .brand__name { color: var(--gold); font-weight: 600; line-height: 1; }
  .brand__word { display: block; font-size: 46px; letter-spacing: 3px; }
  .brand__sub { display: block; font-size: 14px; letter-spacing: 9.5px; margin-top: 6px; }

  .card--front .brand { left: 100px; top: 105px; }
  .website {
    position: absolute; left: 180px; top: 210px;
    color: var(--gold); font-size: 14px; letter-spacing: 2.5px;
  }

  .card--back .brand { left: 34px; top: 100px; gap: 12px; }
  .card--back .brand__mark { width: 54px; height: 54px; border-width: 4px; }
  .card--back .brand__word { font-size: 32px; letter-spacing: 2px; }
  .card--back .brand__sub { font-size: 9.5px; letter-spacing: 4.2px; margin-top: 5px; }

  .person { position: absolute; left: 40px; top: 222px; }
  .person__name { font-size: 22px; font-weight: 700; color: var(--ink); letter-spacing: 0.5px; }
  .person__role { font-size: 16px; color: var(--ink-soft); margin-top: 4px; }

  .contacts {
    position: absolute; left: 322px; top: 66px; width: 224px;
    list-style: none; display: flex; flex-direction: column; gap: 6px;
  }
  .contacts__item { display: flex; align-items: flex-start; gap: 7px; font-size: 11.5px; color: var(--ink-soft); line-height: 18px; white-space: nowrap; }
  .contacts__icon { width: 18px; height: 18px; flex: none; }
</style>
</head>
<body>
<main class="canvas">

  <section class="card card--front" aria-label="Card front">
    <div class="brand">
      <span class="brand__mark"></span>
      <span class="brand__name">
        <span class="brand__word">TORQUEL</span>
        <span class="brand__sub">AUSTRALIA PTY LTD</span>
      </span>
    </div>
    <p class="website">www.torquelaustralia.com.au</p>
  </section>

  <section class="card card--back" aria-label="Card back">
    <div class="brand">
      <span class="brand__mark"></span>
      <span class="brand__name">
        <span class="brand__word">TORQUEL</span>
        <span class="brand__sub">AUSTRALIA PTY LTD</span>
      </span>
    </div>

    <div class="person">
      <p class="person__name">MARCUS HALE</p>
      <p class="person__role">Director</p>
    </div>

    <ul class="contacts">
      <li class="contacts__item">
        <svg class="contacts__icon" viewBox="0 0 18 18" aria-hidden="true"><circle cx="9" cy="9" r="9" fill="var(--gold)"/><path d="M6 5 L8 5 L8.6 7.2 L7.6 8 Q8.5 10 10 10.6 L10.8 9.6 L13 10.2 L13 12 Q9 12.5 6.5 9.5 Q5.5 7.5 6 5 Z" fill="var(--icon-fg)"/></svg>
        <span>02 5550 1847</span>
      </li>
      <li class="contacts__item">
        <svg class="contacts__icon" viewBox="0 0 18 18" aria-hidden="true"><circle cx="9" cy="9" r="9" fill="var(--gold)"/><rect x="6.3" y="4" width="5.4" height="10" rx="1" fill="none" stroke="var(--icon-fg)" stroke-width="1.2"/></svg>
        <span>0400 555 219</span>
      </li>
      <li class="contacts__item">
        <svg class="contacts__icon" viewBox="0 0 18 18" aria-hidden="true"><circle cx="9" cy="9" r="9" fill="var(--gold)"/><rect x="4.5" y="6" width="9" height="6.2" fill="none" stroke="var(--icon-fg)" stroke-width="1.1"/><path d="M4.5 6 L9 9.5 L13.5 6" fill="none" stroke="var(--icon-fg)" stroke-width="1.1"/></svg>
        <span>marcus@torquelaustralia.com.au</span>
      </li>
      <li class="contacts__item">
        <svg class="contacts__icon" viewBox="0 0 18 18" aria-hidden="true"><circle cx="9" cy="9" r="9" fill="var(--gold)"/><path d="M9 14 Q5.5 9.8 5.5 7.6 A3.5 3.5 0 0 1 12.5 7.6 Q12.5 9.8 9 14 Z" fill="var(--icon-fg)"/><circle cx="9" cy="7.6" r="1.3" fill="var(--gold)"/></svg>
        <span>PO Box 318<br>Kelvale NSW 2990</span>
      </li>
    </ul>
  </section>

</main>
</body>
</html>
```